I'm looking for a fresh new design for my business Martin Coldwell Creative.
I am a photographer and videographer.
The card must be easy to print, eye catching and easy to read. It must reflect the fact that I work in a creative area, but not so edgy as to scare away my corporate clients.
Sub text should read Photography, Video, Design
There also needs to be room for phone number and email.

```html
<!DOCTYPE html>
<html lang="en">
<head>
<meta charset="utf-8">
<title>Martin Coldwell Creative – Business Card</title>
<link rel="stylesheet" href="https://fonts.googleapis.com/css2?family=Arimo:wght@400&display=swap">
<style>
  :root {
    --backdrop: #3a3330;
    --card-edge: #0c0c0c;
    --card-glow: #2c2c2c;
    --text-main: #f2f2f2;
    --text-sub: #8e8e8e;
    --accent-red: #9e1f23;
    --divider: #6a6a6a;
  }
  * { margin: 0; padding: 0; box-sizing: border-box; }
  html, body {
    width: 1200px;
    height: 1000px;
    overflow: hidden;
    background: var(--backdrop);
    font-family: "Arimo", Arial, sans-serif;
  }
  .sheet {
    position: relative;
    width: 1200px;
    height: 1000px;
  }
  .card {
    position: absolute;
    left: 295px;
    width: 610px;
    height: 330px;
    background: radial-gradient(ellipse 45% 55% at 50% 45%, var(--card-glow) 0%, #1a1a1a 55%, var(--card-edge) 100%);
    box-shadow: 0 6px 18px rgba(0,0,0,0.45);
  }
  .card--front { top: 150px; }
  .card--back { top: 520px; }

  /* Front */
  .title-block {
    position: absolute;
    left: 50%;
    top: 150px;
    transform: translateX(-50%);
    text-align: center;
  }
  .title-block__row {
    display: flex;
    align-items: center;
    justify-content: center;
    gap: 12px;
  }
  .title-block__square {
    width: 10px;
    height: 10px;
    background: var(--accent-red);
    flex: none;
  }
  .title-block__name {
    color: var(--text-main);
    font-size: 25px;
    letter-spacing: 0.5px;
    line-height: 1;
    white-space: nowrap;
  }
  .title-block__services {
    color: var(--text-sub);
    font-size: 10px;
    letter-spacing: 0.6px;
    margin-top: 6px;
    white-space: nowrap;
  }

  /* Back */
  .identity {
    position: absolute;
    right: 320px;
    top: 143px;
  }
  .identity__name {
    color: var(--text-main);
    font-size: 26px;
    letter-spacing: 1px;
    line-height: 1;
    white-space: nowrap;
  }
  .identity__services {
    color: var(--text-sub);
    font-size: 9.5px;
    letter-spacing: 0.6px;
    margin-top: 3px;
    white-space: nowrap;
  }
  .divider {
    position: absolute;
    left: 318px;
    top: 122px;
    width: 1px;
    height: 88px;
    background: linear-gradient(to bottom, transparent, var(--divider) 30%, var(--divider) 70%, transparent);
  }
  .contact {
    position: absolute;
    left: 357px;
    top: 138px;
    list-style: none;
    color: var(--text-main);
    font-size: 12px;
    letter-spacing: 0.8px;
    line-height: 18px;
  }
</style>
</head>
<body>
<main class="sheet">
  <section class="card card--front" aria-label="Card front">
    <div class="title-block">
      <div class="title-block__row">
        <span class="title-block__square" aria-hidden="true"></span>
        <p class="title-block__name">Martin Coldwell Creative</p>
      </div>
      <p class="title-block__services">PHOTOGRAPHY, VIDEO, DESIGN</p>
    </div>
  </section>

  <section class="card card--back" aria-label="Card back">
    <div class="identity">
      <p class="identity__name">Martin Coldwell</p>
      <p class="identity__services">PHOTOGRAPHY, VIDEO, DESIGN</p>
    </div>
    <div class="divider"></div>
    <ul class="contact">
      <li>(345)-555-0187</li>
      <li>martin.coldwell@coldwellmail.com</li>
      <li>@martin.coldwell</li>
    </ul>
  </section>
</main>
</body>
</html>
```